Wren Hollow Apartments
stationary
Wren Hollow Apartments - Real Estate
Creative Brief
Traditional
Tobias Lindqvist
2408 Wren Hollow Houston TX 77091
tjlindqvist@quellmail.example

```html
<!DOCTYPE html>
<html lang="en">
<head>
<meta charset="utf-8">
<title>Wren Hollow Apartments – Business Card</title>
<link rel="stylesheet" href="https://fonts.googleapis.com/css2?family=Tinos:wght@400;700&display=swap">
<style>
  :root {
    --backdrop: #e4e4e2;
    --brand-green: #2f8a3f;
    --card-white: #ffffff;
    --ink: #3a3a3a;
    --rule: #d6d6d6;
    --shadow: rgba(0, 0, 0, 0.18);
  }
  * { box-sizing: border-box; margin: 0; padding: 0; }
  html, body {
    width: 1200px;
    height: 871px;
    overflow: hidden;
    background: var(--backdrop);
    font-family: "Tinos", "Times New Roman", serif;
  }
  .canvas {
    position: relative;
    width: 1200px;
    height: 871px;
  }
  .card {
    position: absolute;
    left: 300px;
    width: 600px;
    height: 343px;
    box-shadow: 0 10px 26px var(--shadow);
  }
  .card--front {
    top: 70px;
    background: var(--brand-green);
    display: flex;
    align-items: center;
    justify-content: center;
  }
  .card--back {
    top: 473px;
    background: var(--card-white);
    display: flex;
  }
  .brand-name {
    text-align: center;
    font-weight: 400;
    text-transform: uppercase;
    line-height: 1;
  }
  .brand-name__main {
    display: block;
    font-size: 40px;
    letter-spacing: 1px;
  }
  .brand-name__sub {
    display: block;
    margin-top: 8px;
    font-size: 15px;
    letter-spacing: 6px;
  }
  .card--front .brand-name { color: var(--card-white); }
  .card--back .brand-name { color: var(--brand-green); }
  .card--back .brand-name__main { font-size: 34px; }
  .card--back .brand-name__sub { font-size: 13px; letter-spacing: 5px; }

  .back__brand {
    width: 290px;
    display: flex;
    align-items: center;
    justify-content: center;
  }
  .back__divider {
    width: 1px;
    margin: 40px 0;
    background: var(--rule);
  }
  .back__details {
    flex: 1;
    padding: 62px 0 0 34px;
    color: var(--ink);
  }
  .contact-name {
    font-size: 20px;
    font-variant: small-caps;
    letter-spacing: 1px;
    color: var(--brand-green);
    margin-bottom: 34px;
  }
  .contact-address {
    font-size: 15px;
    line-height: 1.45;
    font-style: normal;
    margin-bottom: 12px;
  }
  .contact-line {
    display: flex;
    align-items: center;
    gap: 8px;
    font-size: 15px;
    line-height: 1.6;
  }
  .contact-line svg { flex: none; }
</style>
</head>
<body>
<main class="canvas">
  <section class="card card--front" aria-label="Card front">
    <h1 class="brand-name">
      <span class="brand-name__main">Wren Hollow</span>
      <span class="brand-name__sub">Apartments</span>
    </h1>
  </section>

  <section class="card card--back" aria-label="Card back">
    <div class="back__brand">
      <p class="brand-name">
        <span class="brand-name__main">Wren Hollow</span>
        <span class="brand-name__sub">Apartments</span>
      </p>
    </div>
    <div class="back__divider"></div>
    <div class="back__details">
      <h2 class="contact-name">Tobias Lindqvist</h2>
      <address class="contact-address">
        2408 Wren Hollow<br>
        Houston TX 77091
      </address>
      <p class="contact-line">
        <svg width="12" height="12" viewBox="0 0 24 24" aria-hidden="true">
          <path fill="#2f8a3f" d="M6.6 10.8a15.1 15.1 0 0 0 6.6 6.6l2.2-2.2c.3-.3.7-.4 1-.2 1.1.4 2.3.6 3.6.6.6 0 1 .4 1 1V20c0 .6-.4 1-1 1A17 17 0 0 1 3 4c0-.6.4-1 1-1h3.5c.6 0 1 .4 1 1 0 1.3.2 2.5.6 3.6.1.3 0 .7-.2 1z"/>
        </svg>
        713-555-0148
      </p>
      <p class="contact-line">
        <svg width="12" height="10" viewBox="0 0 24 18" aria-hidden="true">
          <rect x="1" y="1" width="22" height="16" fill="none" stroke="#2f8a3f" stroke-width="2"/>
          <path d="M1 1l11 9 11-9" fill="none" stroke="#2f8a3f" stroke-width="2"/>
        </svg>
        tjlindqvist@quellmail.example
      </p>
    </div>
  </section>
</main>
</body>
</html>
```